Maple Lantern Business Card

Design of business cards

Target Market(s)

We are aiming as small business owners who need anything from basic business structures, website plans, business processes and quality assurance.

Industry/Entity Type

Business

Colors

Designer to choose colors to be used in the design.

Requirements
Nice to have
• I would prefer one side of the card to use the green from the logo. Prefer to have the same font as the logo.

```html
<!DOCTYPE html>
<html lang="en">
<head>
<meta charset="utf-8">
<title>Maple Lantern Business Card</title>
<link rel="stylesheet" href="https://fonts.googleapis.com/css2?family=Marcellus&family=Arimo:wght@400&display=swap">
<style>
  :root {
    --leaf-green: #a9cf46;
    --leaf-green-soft: #c9e08a;
    --paper: #ffffff;
    --ink-grey: #58595b;
    --frame-grey: #4a4a4a;
    --card-edge: #b9b9b9;
  }
  * { margin: 0; padding: 0; box-sizing: border-box; }
  html, body { width: 1200px; height: 1000px; overflow: hidden; background: var(--paper); }
  .board {
    position: relative;
    width: 1200px;
    height: 1000px;
    border: 2px solid var(--frame-grey);
    background: var(--paper);
  }
  .accent-bar {
    position: absolute;
    left: 2px;
    top: 788px;
    width: 29px;
    height: 210px;
    background: var(--leaf-green);
  }
  .card {
    position: absolute;
    left: 268px;
    width: 649px;
    height: 406px;
  }
  .card--front {
    top: 74px;
    background: var(--leaf-green);
    display: flex;
    align-items: center;
    justify-content: center;
  }
  .brand-name {
    font-family: "Marcellus", serif;
    font-weight: 400;
    color: var(--paper);
    font-size: 64px;
    letter-spacing: 1px;
  }
  .card--back {
    top: 518px;
    border: 1px solid var(--card-edge);
    background: linear-gradient(90deg, #ffffff 2%, #eef5dc 25%, var(--leaf-green-soft) 70%, var(--leaf-green) 100%);
  }
  .brand-line {
    position: absolute;
    left: 20px;
    top: 22px;
    display: flex;
    align-items: center;
    gap: 10px;
    font-family: "Marcellus", serif;
    font-weight: 400;
    color: var(--leaf-green);
    font-size: 22px;
  }
  .brand-square {
    width: 14px;
    height: 14px;
    background: var(--leaf-green);
  }
  .holder-name {
    position: absolute;
    left: 216px;
    top: 152px;
    font-family: "Arimo", sans-serif;
    font-size: 44px;
    color: var(--ink-grey);
    line-height: 1;
  }
  .holder-business {
    position: absolute;
    left: 227px;
    top: 208px;
    font-family: "Arimo", sans-serif;
    font-size: 24px;
    color: var(--ink-grey);
    line-height: 1;
  }
</style>
</head>
<body>
  <main class="board">
    <section class="card card--front" aria-label="Card front">
      <span class="brand-name">Maple Lantern</span>
    </section>
    <section class="card card--back" aria-label="Card back">
      <div class="brand-line">
        <span class="brand-square"></span>
        <span>Maple Lantern Consulting</span>
      </div>
      <p class="holder-name">Your Name</p>
      <p class="holder-business">Business name</p>
    </section>
    <div class="accent-bar"></div>
  </main>
</body>
</html>
```